Microsite for a private healthcare provider

The design I need (PSD file) is for a company offering two services:
1. Recruitment of nurses
2. Provider a private health care: prenatal classes, vaccines for travellers
Here's a website we designed and we would like a similar style in terms of layout. Please note there will be about the same amount of content (text) http://lumeravisuel.example/fr
Main menu with 4 sections:
Accueil |Agence de placement | Soins privés | Contact
Links to their social media accounts:
https://twitter.com/Valdoriel
https://www.facebook.com/pages/Valdoriel-Agence-de-placement-en-soins-de-sant%C3%A9/482039571620413
Contact details:
TÉL. (555) 302-4419
TÉLEC. (555) 302-9154
1187 boulevard Ormelande, suite 3400
Ste-Olvanne (Québec), K8W 5M3
Target Market(s)
Nurses looking for a job, Expecting women, People about to travel and seeking vaccines
Industry/Entity Type
Healthcare
Requirements
Must have
- 1- Must be responsive for mobiles and tablets
2 - Pipelette feed
3 - Google maps at the end next to their contact details
4- Two contact forms:
Form for people to send in their resume.
The form title is: Postulez
Fields required:
Nom complet
Courriel
Téléphone
Années d'expérience (with drop down list: 1-2 ans, 3-5 ans, 5 ans et plus)
Choose file (possibility to attach a cv)
Message
Form for requesting information
Form title is: Demande d'informations
Fields are:
Nom complet
Téléphone
Courriel
Message
Nice to have
- Here are some images on Pixvane Images the client likes, you can use for inspiration.
Agence de placement section:
File #40581936
File #6417283
File #8250946
File #5092734
File #47306152
File #39847201
File #26415037
Soins privés section:
File #33782519
File #31940285
File #34617092
File #48053276
File #27360458
File #29518064
File #42870315
File #6783052
File #35104827

```html
<!DOCTYPE html>
<html lang="fr">
<head>
<meta charset="utf-8">
<title>Valdoriel – Soins de santé personnalisés, en privé</title>
<link rel="stylesheet" href="https://fonts.googleapis.com/css2?family=Exo+2:ital,wght@0,400;0,500;0,600;0,700;1,400;1,600&family=Open+Sans:ital,wght@0,400;0,600;1,400&display=swap">
<style>
  :root {
    --blue: #1553a6;
    --blue-dark: #0c3f86;
    --green: #9cb81d;
    --green-dark: #7f9a10;
    --ink: #222222;
    --text: #6f6f6f;
    --hero-text: #3a3a3a;
    --light: #f4f5f6;
    --form-bg: #e3e3e3;
    --field: #eeeeee;
    --field-line: #c9c9c9;
    --footer: #15171b;
    --white: #ffffff;
    --rule: #6c6f75;
  }
  * { box-sizing: border-box; margin: 0; padding: 0; }
  html, body { width: 1200px; height: 2479px; overflow: hidden; }
  body {
    position: relative;
    background: var(--white);
    font-family: "Exo 2", "Trebuchet MS", sans-serif;
    color: var(--text);
  }
  .section { position: absolute; left: 0; width: 1200px; overflow: hidden; }
  .photo { position: absolute; }

  /* Brand */
  .brand { position: absolute; text-align: center; }
  .brand-name {
    display: block;
    font-family: "Exo 2", sans-serif;
    font-weight: 700;
    color: var(--blue);
    line-height: 1;
  }
  .brand-tagline {
    display: block;
    font-family: "Exo 2", sans-serif;
    font-weight: 600;
    font-style: italic;
    color: var(--blue);
    white-space: nowrap;
  }

  /* Hero */
  .hero { top: 0; height: 512px; }
  .hero .photo {
    inset: 0;
    background:
      radial-gradient(ellipse 300px 260px at 220px 130px, rgba(214,190,170,.55), transparent 70%),
      radial-gradient(ellipse 280px 240px at 960px 150px, rgba(205,180,160,.55), transparent 70%),
      radial-gradient(ellipse 260px 200px at 1080px 420px, rgba(190,200,215,.5), transparent 70%),
      linear-gradient(180deg, #eef0f3 0%, #e4e8ec 100%);
  }
  .hero .brand { left: 0; width: 1200px; top: 44px; }
  .hero .brand-name { font-size: 60px; }
  .hero .brand-tagline { font-size: 19px; margin-top: 10px; }
  .hero-title {
    position: absolute; left: 0; top: 199px; width: 1200px;
    text-align: center; font-size: 23px; font-weight: 600; color: var(--blue);
  }
  .hero-text {
    position: absolute; left: 140px; top: 236px; width: 920px;
    text-align: center; font-size: 14.5px; font-weight: 600;
    line-height: 27.5px; color: var(--hero-text);
  }
  .scroll-cue { position: absolute; left: 574px; top: 414px; width: 50px; height: 76px; }

  /* Navigation */
  .site-nav {
    top: 512px; height: 103px; background: var(--white);
    border-bottom: 3px solid #cfd1d3;
    box-shadow: 0 2px 4px rgba(0,0,0,.08);
  }
  .site-nav .brand { left: 126px; top: 20px; text-align: left; }
  .site-nav .brand-name { font-size: 42px; }
  .site-nav .brand-tagline { font-size: 13px; margin-top: 6px; }
  .menu { position: absolute; top: 35px; list-style: none; }
  .menu li { position: absolute; white-space: nowrap; font-size: 21px; font-weight: 600; color: var(--ink); }
  .menu li.current { color: var(--blue); }

  /* Welcome */
  .welcome { top: 618px; height: 258px; background: var(--white); }
  .section-title { font-weight: 600; line-height: 1.1; }
  .section-title .blue { color: var(--blue); }
  .section-title .green { color: var(--green); }
  .welcome .section-title {
    position: absolute; left: 0; width: 1200px; top: 26px;
    text-align: center; font-size: 33px; color: var(--ink);
  }
  .body-text { font-size: 13.5px; font-weight: 600; line-height: 24px; color: var(--text); }
  .welcome .body-text {
    position: absolute; left: 140px; top: 90px; width: 925px; text-align: center;
  }

  /* Services */
  .agency { top: 876px; height: 375px; background: var(--light); }
  .agency .photo {
    left: 126px; top: 12px; width: 494px; height: 363px;
    background:
      radial-gradient(ellipse 140px 180px at 170px 190px, rgba(120,150,200,.45), transparent 75%),
      radial-gradient(ellipse 130px 150px at 400px 230px, rgba(200,205,215,.6), transparent 75%),
      linear-gradient(180deg, #f7f8fa 0%, #e9edf2 100%);
  }
  .agency .section-title { position: absolute; left: 640px; top: 26px; font-size: 32px; }
  .agency .body-text { position: absolute; left: 640px; top: 80px; width: 432px; line-height: 23.6px; text-align: justify; }

  .private-care { top: 1251px; height: 381px; background: var(--white); }
  .private-care .section-title { position: absolute; left: 126px; top: 28px; font-size: 32px; }
  .private-care .body-text { position: absolute; left: 126px; top: 82px; width: 470px; line-height: 23.8px; text-align: justify; }
  .private-care .photo {
    left: 628px; top: 0; width: 430px; height: 381px;
    background:
      radial-gradient(ellipse 150px 170px at 220px 160px, rgba(190,150,130,.45), transparent 75%),
      radial-gradient(ellipse 120px 110px at 150px 300px, rgba(235,205,210,.55), transparent 75%),
      linear-gradient(180deg, #f5f5f5 0%, #ebebeb 100%);
  }

  /* Forms */
  .forms { top: 1632px; height: 398px; background: var(--form-bg); }
  .form { position: absolute; top: 0; }
  .form-title { position: absolute; top: 20px; font-size: 31px; font-weight: 600; color: var(--blue); white-space: nowrap; }
  .field {
    position: absolute; height: 32px;
    background: var(--field); border: 1px solid var(--field-line);
    font-family: "Open Sans", sans-serif; font-style: italic; font-size: 11.5px;
    color: #555; padding: 6px 10px; white-space: nowrap;
  }
  .field.message { height: 66px; }
  .button {
    position: absolute; height: 40px; border-radius: 3px;
    font-family: "Open Sans", sans-serif; font-weight: 600; font-size: 16px;
    color: var(--white); text-align: center; line-height: 40px;
  }
  .button.apply { background: linear-gradient(180deg, #1f64c2, var(--blue-dark)); }
  .button.submit { background: linear-gradient(180deg, #a9c427, var(--green-dark)); }

  /* Footer */
  .site-footer { top: 2030px; height: 449px; }
  .site-footer > .photo {
    inset: 0;
    background:
      radial-gradient(ellipse 400px 200px at 900px 100px, rgba(70,75,90,.6), transparent 70%),
      radial-gradient(ellipse 400px 200px at 200px 380px, rgba(60,60,70,.5), transparent 70%),
      linear-gradient(180deg, #2a2d33 0%, var(--footer) 100%);
  }
  .map {
    position: absolute; left: 161px; top: 37px; width: 376px; height: 376px; border-radius: 50%;
    border: 6px solid #d9d9d9;
    background: radial-gradient(circle at 50% 45%, #f2efe9 0%, #e6e3dc 100%);
  }
  .site-footer .brand { left: 615px; top: 44px; text-align: left; }
  .site-footer .brand-name { font-size: 60px; }
  .site-footer .brand-tagline { font-size: 16px; margin-top: 8px; font-style: normal; }
  .footer-heading {
    position: absolute; top: 176px; font-size: 19px; font-weight: 600; color: var(--white);
    padding-bottom: 10px; border-bottom: 1px solid var(--rule); white-space: nowrap;
  }
  .address {
    position: absolute; left: 628px; top: 230px; font-style: normal;
    font-family: "Open Sans", sans-serif; font-size: 13px; line-height: 19px; color: var(--white);
    white-space: nowrap;
  }
  .address .label { color: var(--green); }
  .address .gap { display: block; height: 9px; }
  .social { position: absolute; left: 865px; top: 244px; list-style: none; }
  .social li { display: flex; align-items: center; height: 46px; margin-bottom: 10px; font-size: 19px; font-weight: 500; color: var(--white); }
  .social .dot { width: 46px; height: 46px; border-radius: 50%; margin-right: 14px; }
  .social .dot.primary { background: #3b5da8; border: 2px solid #d3d8e3; }
  .social .dot.secondary { background: #e4e6e9; border: 2px solid #b6b9bd; }
  .footer-line { position: absolute; left: 603px; top: 380px; width: 471px; height: 1px; background: var(--rule); }
  .legal {
    position: absolute; left: 626px; top: 395px;
    font-family: "Open Sans", sans-serif; font-size: 12px; color: var(--white); white-space: nowrap;
  }
  .legal .brand-mention { color: var(--blue); }
  .legal .policy { color: var(--green); margin-left: 12px; }
  .legal .sep { margin: 0 10px; }
</style>
</head>
<body>

<header class="section hero">
  <div class="photo" role="img" aria-label="Photo floue d'une infirmière et d'une patiente en arrière-plan"></div>
  <div class="brand">
    <span class="brand-name">Valdoriel</span>
    <span class="brand-tagline">Soins de santé personnalisés, en privé</span>
  </div>
  <h1 class="hero-title">Lorem ipsum dolor sit amet, consectetur adipiscing elit. Cras hendrerit</h1>
  <p class="hero-text">leo mauris mollis ipsum, et egestas nisl purus ut massa. Nulla mollis, massa ac porta mollis, ligula velit vestibulum leo, sed pretium nisl est vel tortor. Donec at lobortis felis. Nunc sit amet congue arcu. Fusce sodales, mi non aliquet aliquam, nisl elit mattis diam, id gravida magna sem eu tortor. Aenean ligula est, sollicitudin sit amet tellus iaculis, venenatis venenatis felis. Donec est nunc, iaculis sed lacinia nec, aliquet sit amet nisi. Aliquam auctor dolor placerat purus tincidunt tincidunt. Ut pharetra purus eros, a malesuada risus elementum quis.</p>
  <svg class="scroll-cue" viewBox="0 0 50 76" aria-hidden="true">
    <g fill="none" stroke-width="7" stroke-linejoin="miter">
      <polyline points="4,6 25,20 46,6" stroke="#8d8d8d"/>
      <polyline points="4,28 25,42 46,28" stroke="#5c5c5c"/>
      <polyline points="4,50 25,64 46,50" stroke="#333333"/>
    </g>
  </svg>
</header>

<nav class="section site-nav">
  <div class="brand">
    <span class="brand-name">Valdoriel</span>
    <span class="brand-tagline">Soins de santé personnalisés, en privé</span>
  </div>
  <ul class="menu">
    <li class="current" style="left:474px">Accueil</li>
    <li style="left:577px">Agence de placement</li>
    <li style="left:822px">Soins privés</li>
    <li style="left:982px">Contact</li>
  </ul>
</nav>

<section class="section welcome">
  <h2 class="section-title">Welcome To <span class="blue">Valdoriel</span></h2>
  <p class="body-text">Lorem ipsum dolor sit amet, consectetur adipiscing elit. Cras hendrerit, felis sed cursus iaculis, leo mauris mollis ipsum, et egestas nisl purus ut massa. Nulla mollis, massa ac porta mollis, ligula velit vestibulum leo, sed pretium nisl est vel tortor. Donec at lobortis felis. Nunc sit amet congue arcu. Fusce sodales, mi non aliquet aliquam, nisl elit mattis diam, id gravida magna sem eu tortor. Aenean ligula est, sollicitudin sit amet tellus iaculis, venenatis venenatis felis. Donec est nunc, iaculis sed lacinia nec, aliquet sit amet nisi. Aliquam auctor dolor placerat purus tincidunt tincidunt. Ut pharetra purus eros, a malesuada risus elementum quis. Integer posuere urna et purus volutpat, quis laoreet nisl cursus. Nullam tristique tortor eu mauris iaculis porta.</p>
</section>

<section class="section agency">
  <div class="photo" role="img" aria-label="Photo d'une infirmière en blouse blanche avec un médecin et une patiente en arrière-plan"></div>
  <h2 class="section-title"><span class="blue">Agence de</span> <span class="green">placement</span></h2>
  <p class="body-text">Lorem ipsum dolor sit amet, consectetur adipiscing elit. Cras hendrerit, felis sed cursus iaculis, leo mauris mollis ipsum, et egestas nisl purus ut massa. Nulla mollis, massa ac porta mollis, ligula velit vestibulum leo, sed pretium nisl est vel tortor. Donec at lobortis felis. Nunc sit amet congue arcu. Fusce sodales, mi non aliquet aliquam, nisl elit mattis diam, id gravida magna sem eu tortor. Aenean ligula est, sollicitudin sit amet tellus iaculis, venenatis venenatis felis. Donec est nunc, iaculis sed lacinia nec, aliquet sit amet nisi. Aliquam auctor dolor placerat purus tincidunt tincidunt. Ut pharetra purus eros, a malesuada risus elementum quis. Integer tortor eu mauris iaculis porta.</p>
</section>

<section class="section private-care">
  <h2 class="section-title"><span class="blue">Valdoriel</span></h2>
  <p class="body-text">Lorem ipsum dolor sit amet, consectetur adipiscing elit. Cras hendrerit, felis sed cursus iaculis, leo mauris mollis ipsum, et egestas nisl purus ut massa. Nulla mollis, massa ac porta mollis, ligula velit vestibulum leo, sed pretium nisl est vel tortor. Donec at lobortis felis. Nunc sit amet congue arcu. Fusce sodales, mi non aliquet aliquam, nisl elit mattis diam, id gravida magna sem eu tortor. Aenean ligula est, sollicitudin sit amet tellus iaculis, venenatis venenatis felis. Donec est nunc, iaculis sed lacinia nec, aliquet sit amet nisi. Aliquam auctor dolor placerat purus tincidunt tincidunt. Ut pharetra purus eros, a malesuada risus elementum quis. Integer tortor eu mauris iaculis porta.</p>
  <div class="photo" role="img" aria-label="Photo d'une mère tenant son bébé contre elle"></div>
</section>

<section class="section forms">
  <form class="form apply-form" style="left:126px">
    <h2 class="form-title" style="left:0">Postulez</h2>
    <div class="field" style="left:0;top:79px;width:446px">Nom complet :</div>
    <div class="field" style="left:0;top:120px;width:446px">Courriel :</div>
    <div class="field" style="left:0;top:161px;width:446px">Téléphone :</div>
    <div class="field" style="left:0;top:202px;width:219px">Années d'expérience :</div>
    <div class="field" style="left:227px;top:202px;width:219px">Choose file :</div>
    <div class="field message" style="left:0;top:241px;width:446px">Message :</div>
    <div class="button apply" style="left:0;top:320px;width:84px">Apply</div>
  </form>
  <form class="form info-form" style="left:626px">
    <h2 class="form-title" style="left:0">Demande d'informations</h2>
    <div class="field" style="left:0;top:79px;width:448px">Nom complet :</div>
    <div class="field" style="left:0;top:124px;width:448px">Téléphone :</div>
    <div class="field" style="left:0;top:168px;width:448px">Courriel :</div>
    <div class="field message" style="left:0;top:211px;width:448px;height:70px">Message :</div>
    <div class="button submit" style="left:2px;top:302px;width:94px">Submit</div>
  </form>
</section>

<footer class="section site-footer">
  <div class="photo" role="img" aria-label="Photo floue et sombre d'une foule en arrière-plan"></div>
  <div class="map" role="img" aria-label="Carte de localisation du bureau"></div>
  <div class="brand">
    <span class="brand-name">Valdoriel</span>
    <span class="brand-tagline">Soins de santé personnalisés, en privé</span>
  </div>
  <h3 class="footer-heading" style="left:628px">Coordonnées</h3>
  <address class="address">
    1187 boulevard Ormelande,<br>
    suite 3400<br>
    Ste-Olvanne (Québec), K8W 5M3
    <span class="gap"></span>
    <span class="label">TÉL :</span> (555) 302-4419<br>
    <span class="gap"></span>
    <span class="label">TÉLEC :</span> (555) 302-9154
  </address>
  <h3 class="footer-heading" style="left:865px;width:200px">Visitez notre page</h3>
  <ul class="social">
    <li><span class="dot primary"></span>Amilia</li>
    <li><span class="dot secondary"></span>Pipelette</li>
  </ul>
  <div class="footer-line"></div>
  <p class="legal">© 2013 <span class="brand-mention">Valdoriel</span>. All rights reserved. <span class="policy">Privacy Policy</span><span class="sep">/</span>Terms of use</p>
</footer>

</body>
</html>
```